Mineral Drinking Water Label Design

We need a label design for a new bottled drinking water based in (either Pwani or Dar Es Salaam, decision is not yet finalized), Tanzania on the coast of East Africa.

We will use underground aquifers as our only source of raw water(pre treated water).

Which will then be treated through osmosis process, then the mineral water will be bottled in standard 500ml, 1000ml and 1500 ml plastic PET bottles for customer consumption.

We have a vision of expanding our supply network to cover the entire country. Therefore, we expect the label to communicate trust, purity, cleanliness, healthiness of water contained.

The uniqueness and attractiveness of the label/logo is of utmost importance.

With regards to water brand name, we prefer that you use your own imagination and creativity to come up with a name that might be more suited to your individual design.

Note: Different shades of blue are mainly associated with drinking water in Tanzania, however feel free to use any other colors.

Target Market(s)

Upper Class citizens, Hotels, Large Supermarkets etc

Font styles to use
Script

Colors

Designer to choose colors to be used in the design.

```html
<!DOCTYPE html>
<html lang="en">
<head>
<meta charset="UTF-8">
<title>Kivua Mineral Water – Label</title>
<link rel="stylesheet" href="https://fonts.googleapis.com/css2?family=Marcellus&family=Montserrat:wght@500;600&display=swap">
<style>
  :root {
    --backdrop: #8e8f91;
    --white: #ffffff;
    --blue-deep: #0a5fb4;
    --blue-mid: #1589d6;
    --blue-bright: #15a6e6;
    --blue-light: #3fb7ea;
    --navy: #1d2f86;
  }
  * { margin: 0; padding: 0; box-sizing: border-box; }
  html, body {
    width: 1082px;
    height: 1200px;
    overflow: hidden;
    background: var(--backdrop);
  }
  .canvas {
    position: relative;
    width: 1082px;
    height: 1200px;
  }
  .wordmark {
    position: absolute;
    top: 200px;
    left: 0;
    width: 100%;
    text-align: center;
    font-family: "Marcellus", serif;
    font-size: 118px;
    letter-spacing: 4px;
    color: var(--white);
    line-height: 1;
  }
  .label {
    position: absolute;
    top: 430px;
    left: 311px;
    width: 460px;
    height: 370px;
    filter: drop-shadow(0 0 14px rgba(255,255,255,0.85)) drop-shadow(0 0 26px rgba(255,255,255,0.45));
  }
  .label svg { position: absolute; inset: 0; }
  .label-content {
    position: absolute;
    inset: 0;
    display: flex;
    flex-direction: column;
    align-items: center;
    justify-content: center;
    padding-top: 10px;
  }
  .label-name {
    font-family: "Marcellus", serif;
    font-size: 92px;
    letter-spacing: 3px;
    color: var(--white);
    line-height: 1;
  }
  .label-product {
    display: flex;
    align-items: center;
    gap: 10px;
    margin-top: 18px;
    font-family: "Montserrat", sans-serif;
    font-weight: 500;
    font-size: 18px;
    letter-spacing: 3.5px;
    color: var(--white);
  }
  .label-product .rule {
    width: 42px;
    height: 2px;
    background: var(--white);
  }
  .label-origin {
    margin-top: 30px;
    font-family: "Montserrat", sans-serif;
    font-weight: 600;
    font-size: 14px;
    letter-spacing: 4px;
    color: var(--navy);
  }
  .volume {
    position: absolute;
    top: 892px;
    left: 0;
    width: 100%;
    text-align: center;
    font-family: "Montserrat", sans-serif;
    font-weight: 600;
    font-size: 15px;
    letter-spacing: 3px;
    color: var(--navy);
  }
</style>
</head>
<body>
<main class="canvas">
  <h1 class="wordmark">KIVUA</h1>

  <section class="label">
    <svg width="460" height="370" viewBox="0 0 460 370" role="img" aria-label="Faceted blue crystal pattern background">
      <defs>
        <linearGradient id="labelFill" x1="0" y1="0" x2="1" y2="1">
          <stop offset="0" stop-color="var(--blue-deep)"/>
          <stop offset="0.45" stop-color="var(--blue-mid)"/>
          <stop offset="0.75" stop-color="var(--blue-bright)"/>
          <stop offset="1" stop-color="var(--blue-light)"/>
        </linearGradient>
      </defs>
      <polygon points="100,14 360,14 446,185 360,356 100,356 14,185"
               fill="url(#labelFill)" stroke="url(#labelFill)"
               stroke-width="26" stroke-linejoin="round"/>
    </svg>
    <div class="label-content">
      <div class="label-name">KIVUA</div>
      <div class="label-product"><span class="rule"></span>MINERAL WATER<span class="rule"></span></div>
      <div class="label-origin">TANZANIA - AFRICA</div>
    </div>
  </section>

  <p class="volume">500 ML (16.9 FL OZ)</p>
</main>
</body>
</html>
```